Brightwell Auto Care 4x9 Rack Card

Design a 4" wide by 9" tall rack card printed front and back using the copy, logo and images uploaded below. I am also uploading a current flyer so you can see the typestyles we use. I will get the exact name of the font for you ASAP. Also will be uploading some before and after pictures for the back of the rack card

Target Market(s)

Affluent consumers who need their car cleaned and detailed in a meticulous fashion

Requirements
Must have
• Under the logo, put the words...... Premium Steam Detailing & Ceramic Coating.........also put ther following wording on the front side: Get Steamed! We use steam to clean your vehicle helping save millions of gallons of water and protecting our rivers, streams and lakes from runoff.
Nice to have
• a screened back background of hexagons might be nice

```html
<!DOCTYPE html>
<html lang="en">
<head>
<meta charset="utf-8">
<title>Brightwell Auto Care – Rack Card</title>
<link href="https://fonts.googleapis.com/css2?family=Montserrat:wght@400;500;600;700;800&family=Oswald:wght@400;500&display=swap" rel="stylesheet">
<style>
  :root {
    --blue: #4a82c6;
    --green: #6fae4b;
    --paper: #f3f4f7;
    --ink: #232323;
    --stage: #d9d9d9;
    --photo-dark: #1f2a24;
    --photo-mid: #5d6b73;
  }
  * { box-sizing: border-box; margin: 0; padding: 0; }
  html, body { width: 1200px; height: 1200px; overflow: hidden; }
  body { background: var(--stage); position: relative; font-family: "Montserrat", sans-serif; color: var(--ink); }

  .rack-card {
    position: absolute; top: 92px; width: 452px; height: 1015px;
    background: var(--paper); overflow: hidden;
    box-shadow: 0 6px 18px rgba(0,0,0,.18);
  }
  .rack-card--front { left: 130px; }
  .rack-card--back { left: 617px; }

  .hero-photo {
    position: absolute; left: 0; top: 0; width: 452px; height: 426px;
    background: linear-gradient(160deg, #2b332c 0%, #8e979c 45%, #2f5fb0 75%, #1c2a22 100%);
  }
  .rack-card--back .hero-photo {
    background: linear-gradient(150deg, #8c8a6e 0%, #c9c2a2 30%, #3b3f45 60%, #2d5db4 85%, #1b2126 100%);
  }

  .brand {
    position: absolute; top: 478px; left: 0; width: 100%;
    display: flex; align-items: center; justify-content: center; gap: 10px;
  }
  .brand__dot { width: 28px; height: 28px; border-radius: 50%; background: var(--green); }
  .brand__name { font-weight: 700; font-size: 25px; color: var(--blue); letter-spacing: .5px; }

  .headline {
    position: absolute; top: 556px; left: 0; width: 100%; text-align: center;
    font-size: 25.5px; line-height: 28px; font-weight: 600; color: var(--green);
  }
  .headline strong { font-weight: 800; color: var(--blue); }

  .tagline {
    position: absolute; top: 636px; width: 100%; text-align: center;
    font-family: "Oswald", sans-serif; font-weight: 500; font-size: 21px; color: var(--blue); letter-spacing: .5px;
  }
  .tagline__rule { position: absolute; top: 667px; left: 199px; width: 44px; height: 1.5px; background: var(--green); }
  .mission {
    position: absolute; top: 673px; left: 30px; width: 392px; text-align: center;
    font-size: 12.3px; line-height: 15.3px; letter-spacing: .3px;
  }
  .mission b { font-weight: 700; }

  .locations {
    position: absolute; top: 743px; left: 22px; width: 407px; height: 104px;
    border: 1px solid var(--blue); text-align: center; font-size: 12px; line-height: 15px; letter-spacing: .3px;
  }
  .locations__pin { position: absolute; top: -11px; left: 192px; width: 22px; height: 22px; background: var(--paper); }
  .locations__item { position: absolute; left: 22px; width: 363px; }
  .locations__item--a { top: 20px; }
  .locations__item--b { top: 53px; border-top: 1px solid var(--blue); padding-top: 4px; }
  .locations__item--c { top: 75px; border-top: 1px solid var(--blue); padding-top: 4px; }

  .call-bar {
    position: absolute; top: 858px; left: 22px; width: 407px; height: 30px; background: var(--green);
    display: flex; align-items: center; justify-content: center; gap: 8px;
    font-family: "Oswald", sans-serif; font-size: 17px; color: #fff; letter-spacing: .8px;
  }
  .call-bar__rule { width: 24px; height: 1px; background: #fff; }

  .phones { position: absolute; top: 899px; left: 22px; width: 418px; display: flex; }
  .phone { padding-right: 16px; }
  .phone + .phone { border-left: 1px solid var(--blue); padding-left: 17px; }
  .phone__city { font-size: 12px; color: var(--blue); font-weight: 500; letter-spacing: .3px; }
  .phone__number { font-family: "Oswald", sans-serif; font-size: 17px; letter-spacing: .6px; margin-top: 2px; }

  .slogan-band { position: absolute; left: 0; bottom: 0; width: 452px; height: 70px; }
  .slogan-band svg { position: absolute; inset: 0; }
  .slogan-band__text {
    position: absolute; left: 0; top: 20px; width: 100%; text-align: center;
    font-family: "Oswald", sans-serif; font-weight: 500; font-size: 27px; color: #fff; letter-spacing: .6px;
  }

  .result-photo { position: absolute; top: 563px; width: 198px; height: 142px; box-shadow: 0 1px 3px rgba(0,0,0,.2); overflow: hidden; }
  .result-photo--interior { left: 22px; }
  .result-photo--engine { left: 231px; }
  .result-photo__image { height: 115px; background: linear-gradient(135deg, #3c4148, #9aa0a6 55%, #2a2d31); }
  .result-photo--engine .result-photo__image { background: linear-gradient(135deg, #2b2c2e, #8a6a3c 40%, #4a4d52 70%, #1d1e20); }
  .result-photo__labels { display: flex; height: 27px; font-family: "Oswald", sans-serif; font-size: 14px; color: #fff; letter-spacing: .8px; }
  .result-photo__labels span { flex: 1; display: flex; align-items: center; justify-content: center; }
  .result-photo--interior .result-photo__labels { background: linear-gradient(100deg, var(--green) 55%, var(--blue) 55%); }
  .result-photo--engine .result-photo__labels { background: linear-gradient(100deg, var(--blue) 44%, var(--green) 44%); }

  .price-list { position: absolute; top: 716px; left: 22px; width: 407px; list-style: none; }
  .price-list li {
    border-bottom: 1px solid var(--blue); font-size: 14.3px; font-weight: 500; letter-spacing: .3px;
    padding: 4px 0 3px; line-height: 20px;
  }
  .price-list li.two-line { line-height: 22px; padding-top: 4px; }
  .price-list .normal { font-weight: 400; }
  .price { font-family: "Oswald", sans-serif; font-weight: 400; color: var(--blue); font-size: 18.5px; margin: 0 5px; }
</style>
</head>
<body>

<section class="rack-card rack-card--front">
  <div class="hero-photo" role="img" aria-label="Detailer in a blue polo wiping the hood of a silver sports car in a parking garage, framed in a hexagon grid"></div>

  <div class="brand"><span class="brand__dot"></span><span class="brand__name">Brightwell Auto Care</span></div>

  <h1 class="headline"><strong>PREMIUM</strong> STEAM DETAILING<br>&amp; CERAMIC <strong>COATING</strong></h1>

  <h2 class="tagline">GET STEAMED!</h2>
  <div class="tagline__rule"></div>
  <p class="mission">We use <b>steam to clean</b> your vehicle helping save <b>millions of gallons of water</b> and protecting our <b>rivers, streams and lakes</b> from runoff.</p>

  <div class="locations">
    <svg class="locations__pin" viewBox="0 0 22 22" aria-hidden="true">
      <circle cx="11" cy="11" r="10.5" fill="#6fae4b"/>
      <path d="M11 5.5a3.8 3.8 0 0 0-3.8 3.8c0 2.8 3.8 7 3.8 7s3.8-4.2 3.8-7A3.8 3.8 0 0 0 11 5.5z" fill="none" stroke="#fff" stroke-width="1.2"/>
      <circle cx="11" cy="9.3" r="1.3" fill="none" stroke="#fff" stroke-width="1.1"/>
    </svg>
    <p class="locations__item locations__item--a">1420 Larkspur Avenue @ The Larkspur<br>Commons, Boulder</p>
    <p class="locations__item locations__item--b">52 Aspenglen Lane, Snowmass Village</p>
    <p class="locations__item locations__item--c">316 Riverbend Rd, #108 Avon</p>
  </div>

  <div class="call-bar"><span class="call-bar__rule"></span>CALL FOR INFORMATION &amp; SCHEDULING<span class="call-bar__rule"></span></div>

  <div class="phones">
    <div class="phone"><div class="phone__city">Boulder</div><div class="phone__number">(720) 555-0142</div></div>
    <div class="phone"><div class="phone__city">Aspen / Snowmass</div><div class="phone__number">(970) 555-0187</div></div>
    <div class="phone"><div class="phone__city">Vail</div><div class="phone__number">(970) 555-0163</div></div>
  </div>

  <div class="slogan-band">
    <svg viewBox="0 0 452 70" aria-hidden="true">
      <path fill="#4a82c6" d="M0 8 H12 L17 0 H32 L37 8 H53 L58 0 H73 L78 8 H94 L99 0 H114 L119 8 H135 L140 0 H155 L160 8 H176 L181 0 H196 L201 8 H217 L222 0 H237 L242 8 H258 L263 0 H278 L283 8 H299 L304 0 H319 L324 8 H340 L345 0 H360 L365 8 H381 L386 0 H401 L406 8 H422 L427 0 H442 L447 8 H452 V70 H0 Z"/>
    </svg>
    <p class="slogan-band__text">“ FALL IN LOVE WITH YOUR CAR AGAIN! ”</p>
  </div>
</section>

<section class="rack-card rack-card--back">
  <div class="hero-photo" role="img" aria-label="Detailer in a cap steam-cleaning the front grille of a luxury car, framed in a hexagon grid"></div>

  <div class="brand"><span class="brand__dot"></span><span class="brand__name">Brightwell Auto Care</span></div>

  <figure class="result-photo result-photo--interior">
    <div class="result-photo__image" role="img" aria-label="Car seat interior shown before and after steam cleaning"></div>
    <div class="result-photo__labels"><span>BEFORE</span><span>AFTER</span></div>
  </figure>
  <figure class="result-photo result-photo--engine">
    <div class="result-photo__image" role="img" aria-label="Engine bay with leaves shown before and after steam cleaning"></div>
    <div class="result-photo__labels"><span>BEFORE</span><span>AFTER</span></div>
  </figure>

  <ul class="price-list">
    <li>Premium Steam Washes starting at <span class="price">$100</span> and up</li>
    <li>Full Steam Detailing starting at <span class="price">$275</span> and up</li>
    <li class="two-line">Paint Correction <span class="normal">(multi-stage polishing)</span> starting<br>at <span class="price">$650</span> and up</li>
    <li>Headlight Restoration : <span class="price">$110</span></li>
    <li>Engine Steam Cleaning : <span class="price">$75</span></li>
    <li>Ceramic Coating : <span class="price">CALL OR VISIT US FOR A QUOTE</span></li>
  </ul>

  <div class="slogan-band">
    <svg viewBox="0 0 452 70" aria-hidden="true">
      <path fill="#6fae4b" d="M0 8 H12 L17 0 H32 L37 8 H53 L58 0 H73 L78 8 H94 L99 0 H114 L119 8 H135 L140 0 H155 L160 8 H176 L181 0 H196 L201 8 H217 L222 0 H237 L242 8 H258 L263 0 H278 L283 8 H299 L304 0 H319 L324 8 H340 L345 0 H360 L365 8 H381 L386 0 H401 L406 8 H422 L427 0 H442 L447 8 H452 V70 H0 Z"/>
    </svg>
    <p class="slogan-band__text">“ FALL IN LOVE WITH YOUR CAR AGAIN! ”</p>
  </div>
</section>

</body>
</html>
```